COFFE MAKER NEEDS TO MAKE VECTOR OR CURVES FROM IMAGE OF THE LOGO

Hi,

Im a coffee maker and I have all my brand (logo, fonts, etc) in vector or curves. Some person did the coffee bag desing of the product with this vectors i have BUT there is a second bag (the black one) where i lost the illustrator file, i only have the image of it.

WHAT EXACTLY I NEED: The Illustrator (i think new desing) of the black-golden coffe bag im sharing in this project

WHAT CAN I GIVE? the illustrator files of the logo, i have the vectors of the brand

```html
<!DOCTYPE html>
<html lang="es">
<head>
<meta charset="utf-8">
<title>Café Montaña – Solera 1974 bag front</title>
<link rel="stylesheet" href="https://fonts.googleapis.com/css2?family=Josefin+Sans:wght@400;600&display=swap">
<style>
  :root {
    --gold-light: #d0a36b;
    --gold-mid: #c0935d;
    --gold-deep: #a87946;
    --black: #040404;
    --graphite: #4a4a4a;
    --charcoal: #1c1c1c;
    --label-white: #ffffff;
    --ink: #2e2e2e;
    --gold-text: #c08a4f;
  }
  html, body {
    margin: 0;
    padding: 0;
    width: 1200px;
    height: 897px;
    overflow: hidden;
    background: var(--black);
  }
  .bag {
    position: relative;
    width: 1200px;
    height: 897px;
    overflow: hidden;
    font-family: "Josefin Sans", sans-serif;
  }
  .side-panel {
    position: absolute;
    top: 0;
    height: 897px;
    background: linear-gradient(180deg,
      var(--gold-mid) 0%, var(--gold-deep) 26%, var(--gold-mid) 34%,
      var(--gold-deep) 48%, var(--gold-light) 60%, var(--gold-mid) 72%,
      var(--gold-light) 86%, var(--gold-deep) 100%);
  }
  .side-panel--left { left: 0; width: 282px; }
  .side-panel--right { left: 919px; width: 281px; }
  .front-panel {
    position: absolute;
    left: 282px;
    top: 0;
    width: 637px;
    height: 897px;
    background: linear-gradient(180deg,
      var(--black) 0%, var(--graphite) 15%, var(--charcoal) 24%,
      var(--black) 32%, var(--charcoal) 45%, var(--graphite) 64%,
      var(--charcoal) 82%, var(--charcoal) 100%);
  }
  .name-label {
    position: absolute;
    left: 366px;
    top: 0;
    width: 463px;
    height: 213px;
    background: var(--label-white);
    box-shadow: 2px 3px 6px rgba(0,0,0,0.6);
    display: flex;
    align-items: center;
    justify-content: center;
  }
  .name-label__brand {
    margin: 0;
    padding-left: 0.6em;
    font-weight: 600;
    font-size: 23px;
    letter-spacing: 0.6em;
    color: var(--ink);
    text-transform: uppercase;
  }
  .emblem-ring {
    position: absolute;
    left: 345px;
    top: 309px;
    width: 510px;
    height: 510px;
    border-radius: 50%;
    background: radial-gradient(circle,
      rgba(192,138,79,0) 68%, rgba(192,138,79,0.28) 78%,
      rgba(192,138,79,0.12) 92%, rgba(192,138,79,0) 100%);
  }
  .product-name {
    position: absolute;
    left: 345px;
    top: 309px;
    width: 510px;
    height: 510px;
    display: flex;
    align-items: center;
    justify-content: center;
    gap: 14px;
  }
  .product-name__text {
    margin: 0;
    font-weight: 400;
    font-size: 52px;
    letter-spacing: 0.04em;
    color: var(--gold-text);
    text-transform: uppercase;
    text-align: center;
    line-height: 1.1;
  }
  .product-name__dot {
    width: 14px;
    height: 14px;
    border-radius: 50%;
    background: var(--gold-text);
  }
</style>
</head>
<body>
  <main class="bag">
    <div class="side-panel side-panel--left" role="img" aria-label="Gold side gusset with topographic contour-line pattern"></div>
    <div class="front-panel" role="img" aria-label="Black front panel with topographic contour-line pattern"></div>
    <div class="side-panel side-panel--right" role="img" aria-label="Gold side gusset with topographic contour-line pattern"></div>

    <header class="name-label">
      <h1 class="name-label__brand">Café Montaña</h1>
    </header>

    <div class="emblem-ring" role="img" aria-label="Ring of radiating gold dots around the product name"></div>
    <div class="product-name">
      <p class="product-name__text">Solera<br>1974</p>
      <span class="product-name__dot"></span>
    </div>
  </main>
</body>
</html>
```